Home page web design for a lawn specialist business

-The design must be based around the attached HPID (home page information design) called Turf Haven HPID. I've attached Word and PDF versions - these are the same. The table boxes are just for approximate placement of information and you can use boxes and bold shapes for this design.

All fonts used in the HPID are only examples - you can use any Google font you wish.

- Text that is in orange is for your information only. Text to go on the design is black. Some instructions are in the HPID. Please be creative!

-The design needs to be modern and exciting - colours are to be the green of the logo, and white ...and then choose dark green, or dark grey or black.

Logo - attached (it's not great quality but don't worry, we'll replace it later)

- I've provided the images for the galleries - they are labelled and will match the name in the HPID. Please use the supplied images!

- Examples of some websites that have great design... don't copy them please but they are similar in look to what we are after....
www.kelbrinworks.co.nz
http://www.rimsafe-guarding.co.nz/
http://www.brightnest.wb.gs/

Important: Width of content will be 1280 pixels when implemented as a web page but the winning design will need to supplied be on a 2000 pixel wide background so nav bars and background can extend outside the 1280 width.
Header height (without nav bar) 150-160 pixels.

We don't comment on individual designs but will choose a winning design promptly.

Industry/Entity Type

Business

Number of Pages Required

1 page

Font styles to use
Sans Serif

Requirements
Must have
• clean, modern, well-spaced design

```html
<!DOCTYPE html>
<html lang="en">
<head>
<meta charset="utf-8">
<title>Turf Haven – Lawn specialists</title>
<link href="https://fonts.googleapis.com/css2?family=Lato:wght@400;700&display=swap" rel="stylesheet">
<style>
:root{
  --green:#78a500;
  --green-dark:#5f8700;
  --ink:#111;
  --text:#333;
  --grey-bg:#f1f1f1;
  --white:#fff;
  --line:rgba(255,255,255,.35);
}
*{box-sizing:border-box;margin:0;padding:0}
html,body{width:1200px;height:2590px;overflow:hidden}
body{font-family:'Lato',sans-serif;color:var(--text);background:var(--white);position:relative}
.wrap{position:relative;width:832px;margin:0 auto;height:100%}

.site-header{height:122px;background:var(--green);color:var(--white)}
.brand{position:absolute;left:4px;top:38px;font-size:34px;font-weight:700;letter-spacing:1px;display:flex;align-items:center;gap:10px}
.brand-dot{width:16px;height:16px;border-radius:50%;background:var(--white)}
.header-info{position:absolute;right:0;top:16px;text-align:right}
.header-info h1{font-size:27px;font-weight:400;line-height:1.1}
.header-info p{font-size:12px;line-height:1.65}
.header-info .phone{font-size:17px;line-height:1.2}

.main-nav{height:40px;background:var(--white);box-shadow:0 3px 3px rgba(0,0,0,.25);position:relative;z-index:2}
.main-nav ul{list-style:none;display:flex;justify-content:center;gap:35px;height:40px;align-items:center;font-size:13px;color:var(--ink)}

.hero{height:395px;display:flex;position:relative}
.hero-photo{flex:1}
.hero-before{background:linear-gradient(160deg,#e7e5df 0%,#d8d4cc 30%,#6f5a4a 55%,#5a4536 100%)}
.hero-after{background:linear-gradient(160deg,#eeeeea 0%,#dadad5 30%,#5da22c 55%,#3f8a1c 100%)}
.hero-tag{position:absolute;top:330px;width:112px;height:42px;background:var(--white);border-radius:3px;box-shadow:0 2px 4px rgba(0,0,0,.3);font-size:15px;color:var(--ink);display:flex;align-items:center;justify-content:center;letter-spacing:.5px}
.hero-tag.before{left:464px}.hero-tag.after{left:623px}

.intro{height:278px;text-align:center;padding-top:34px}
.intro h2{font-size:31px;font-weight:400;color:var(--ink)}
.intro .lead{font-size:14px;color:var(--ink);margin-top:6px}
.intro .body{width:700px;margin:22px auto 0;font-size:11.5px;line-height:1.75;color:var(--ink)}

.services{height:695px;background:var(--grey-bg)}
.service-card{position:absolute;width:405px}
.service-card h3{font-size:20px;font-weight:400;color:var(--ink)}
.service-card .photo{height:139px;margin-top:10px;border-radius:2px}
.service-card p{font-size:12.5px;line-height:1.75;margin-top:10px;color:var(--ink);text-align:justify;height:64px}
.btn{display:inline-flex;align-items:center;justify-content:center;background:var(--green);color:var(--white);font-size:11.5px;font-weight:700;height:36px;padding:0 16px;border-radius:2px;box-shadow:0 2px 2px rgba(0,0,0,.25);letter-spacing:.3px}
.card-1{left:0;top:42px}.card-2{left:426px;top:42px}
.card-3{left:0;top:372px}.card-4{left:426px;top:372px}
.photo-seeding{background:linear-gradient(180deg,#8fa07a 0%,#5e7f56 45%,#3a8c8a 60%,#2f7d7b 100%)}
.photo-sprinkler{background:radial-gradient(circle at 50% 65%,#c6d6a6 0%,#5ea128 35%,#2f6f12 100%)}
.photo-lawn{background:linear-gradient(180deg,#c4c4b4 0%,#9a9a8a 35%,#3f9a22 55%,#2c7d14 100%)}
.photo-pair{display:flex;gap:3px}
.photo-pair span{flex:1}
.photo-pair .a{background:linear-gradient(180deg,#b9b4a8 0%,#8d877c 40%,#3c8d8d 60%,#2d7273 100%)}
.photo-pair .b{background:linear-gradient(180deg,#bbb6aa 0%,#8f8a7e 40%,#4fa22b 60%,#367f18 100%)}

.video-block{height:383px}
.video-block .col-left{position:absolute;left:0;top:33px;width:405px}
.video-block h3{font-size:15px;font-weight:700;color:var(--ink);line-height:1.45}
.video-frame{margin-top:15px;height:247px;position:relative;background:linear-gradient(180deg,#c9ccc4 0%,#7b8a6a 35%,#3e8d22 60%,#2f7116 100%)}
.video-bar{position:absolute;left:0;right:0;bottom:0;height:16px;background:#1b1b1b}
.video-bar i{position:absolute;left:0;top:0;height:3px;width:72px;background:#d22}
.video-block .col-right{position:absolute;left:426px;top:33px;width:405px}
.video-block .col-right h3{font-size:15px}
.rule{width:33px;height:3px;background:var(--ink);margin:16px 0 20px}
.col-right p{font-size:12.5px;line-height:1.75;color:var(--ink);margin-bottom:16px}
.btn-more{width:92px;height:37px;margin-top:24px;padding:0}

.testimonial{height:212px;background:var(--grey-bg)}
.quote{position:absolute;left:0;top:40px;width:420px}
.quote h3{font-size:19px;font-weight:400;color:var(--ink);line-height:1.3}
.quote p{font-size:11.5px;line-height:1.5;margin-top:8px;color:#555}
.quote .who{text-align:right;font-size:11.5px;color:var(--ink);margin-top:14px;line-height:1.45}
.quote .who b{font-weight:700}
.mower-photo{position:absolute;left:442px;top:45px;width:374px;height:124px;background:linear-gradient(100deg,#555 0%,#6b8a3a 35%,#5aa32a 60%,#8ac04a 100%)}

.site-footer{height:465px;background:var(--green);color:var(--white);position:relative;overflow:hidden}
.quick-links{position:absolute;left:0;top:38px;width:192px}
.site-footer h4{font-size:20px;font-weight:400;padding-bottom:10px;border-bottom:1px solid var(--line)}
.quick-links ul{list-style:none;margin-top:6px}
.quick-links li{font-size:12px;height:26.5px;display:flex;align-items:center;gap:12px;border-bottom:1px solid var(--line)}
.quick-links li:last-child{border-bottom:0}
.quick-links li svg{width:8px;height:8px}
.badge{position:absolute;left:214px;top:40px;width:261px;height:275px;background:var(--white);border-radius:3px;display:flex;align-items:center;justify-content:center}
.badge-shape{width:150px;height:150px;border-radius:50%;background:#8fbf3a}
.contact{position:absolute;left:498px;top:38px;width:334px}
.contact p{font-size:13px;line-height:1.45;margin-top:12px}
.form{margin-top:14px;display:grid;grid-template-columns:1fr 1fr;gap:5px}
.field{height:30px;background:var(--white);color:#aaa;font-size:10px;padding:9px 8px}
.field.wide{grid-column:1/3;height:68px}
.btn-call{margin-top:8px;width:120px;height:37px;background:#050505;color:var(--white);font-size:11.5px;font-weight:700;display:flex;align-items:center;justify-content:center}
.grass-strip{position:absolute;left:0;right:0;bottom:0;height:105px;background:linear-gradient(180deg,rgba(120,165,0,0) 0%,#4f8f12 45%,#2f6d08 100%)}
</style>
</head>
<body>

<header class="site-header">
  <div class="wrap">
    <div class="brand"><span class="brand-dot"></span>Turf Haven</div>
    <div class="header-info">
      <h1>Lawn specialists</h1>
      <p>...from ground preparation to lawn aftercare</p>
      <p>Servicing the Auckland region</p>
      <p class="phone">0800 44 62 19</p>
    </div>
  </div>
</header>

<nav class="main-nav">
  <ul>
    <li>Home</li><li>About us</li><li>Services</li><li>Lawn care</li><li>Seasonal care</li>
    <li>Hydroseeding</li><li>FAQs</li><li>Before &amp; After Gallery</li><li>Quote / Contact</li>
  </ul>
</nav>

<section class="hero">
  <div class="hero-photo hero-before" role="img" aria-label="Courtyard with bare prepared soil before seeding"></div>
  <div class="hero-photo hero-after" role="img" aria-label="Same courtyard with a lush green lawn after seeding"></div>
  <span class="hero-tag before">BEFORE</span>
  <span class="hero-tag after">AFTER</span>
</section>

<section class="intro">
  <h2>You can always spot an Turf Haven lawn</h2>
  <p class="lead">It’s the one that turns your neighbours green with envy.</p>
  <p class="body">If you want a lawn or playing field that looks good throughout the year, talk to us. Turf Haven are New Zealand’s experts in high quality grass seeding and lawn maintenance, creating the lushest lawns you’ll ever see. With high-tech equipment, years of experience and expert aftercare, nobody knows grass like Turf Haven<br>There are many factors that influence the quality of a lawn, including seasonality, growing conditions, shade, seed types, and time. A one-size-fits-all solution couldn’t possibly guarantee a great lawn, so we provide personalised advice, a full range of seeding techniques</p>
</section>

<section class="services">
  <div class="wrap">
    <article class="service-card card-1">
      <h3>Grass Seeding Services</h3>
      <div class="photo photo-seeding" role="img" aria-label="Garden freshly hydroseeded with blue-green mulch"></div>
      <p>With a wide range of grass seed applications to choose from, including hydroseeding and instant lawn, there is an option to suit your property and your requirements.</p>
      <span class="btn">MORE ABOUT GRASS SEEDING</span>
    </article>
    <article class="service-card card-2">
      <h3>Lawn Care Maintenance</h3>
      <div class="photo photo-sprinkler" role="img" aria-label="Sprinkler watering a green lawn"></div>
      <p>As well as lawn care services, the team at Turf Haven provides helpful information for regular upkeep of your residential or commercial lawn.</p>
      <span class="btn">MORE ABOUT ONGOING LAWN CARE</span>
    </article>
    <article class="service-card card-3">
      <h3>FAQs About Grass Seeding And Lawn Care</h3>
      <div class="photo photo-lawn" role="img" aria-label="Fenced backyard with a new green lawn"></div>
      <p>For more information, read our frequently asked questions regarding grass seeding and lawn care.</p>
      <span class="btn">GRASS SEEDING &amp; LAWN CARE FAQS</span>
    </article>
    <article class="service-card card-4">
      <h3>Before And After Lawn Photos</h3>
      <div class="photo photo-pair" role="img" aria-label="Backyard before seeding and the same yard after with green lawn"><span class="a"></span><span class="b"></span></div>
      <p>See what you potential new lawn could look like by viewing a range of before and after lawn seeding photos.</p>
      <span class="btn">BEFORE AND AFTER PHOTOS</span>
    </article>
  </div>
</section>

<section class="video-block">
  <div class="wrap">
    <div class="col-left">
      <h3>Watch the video on how Turf Haven can transform your empty spaces into beautiful green grass lawns</h3>
      <div class="video-frame" role="img" aria-label="Video still of a garden with a freshly grown lawn">
        <div class="video-bar"><i></i></div>
      </div>
    </div>
    <div class="col-right">
      <h3>Turf Haven.....</h3>
      <div class="rule"></div>
      <p>For all things grass, you need the best! Turf Haven are skilled specialists when it comes to creating the perfect lawn for your property.</p>
      <p>From pre-seeding preparation to a full range of grass seeding services and lawn after care options, you’ll enjoy a healthy green lawn for many years.</p>
      <p>Selling your property? Turf Haven will add the wow factor to the outdoor areas of your home with a lush green lawn.</p>
      <span class="btn btn-more">MORE</span>
    </div>
  </div>
</section>

<section class="testimonial">
  <div class="wrap">
    <blockquote class="quote">
      <h3>"I would recommend Turf Haven to anyone who wants an amazing lawn"</h3>
      <p>“Testimonial here about how great Turf Haven were to deal with and how they are so happy with the lawn and the after care services etc etc.”</p>
      <div class="who"><b>Dana Whitfield</b><br><b>Homeowner, Albany</b></div>
    </blockquote>
    <div class="mower-photo" role="img" aria-label="Lawn mower cutting a striped green lawn"></div>
  </div>
</section>

<footer class="site-footer">
  <div class="wrap">
    <div class="quick-links">
      <h4>Quick Links</h4>
      <ul>
        <li><svg viewBox="0 0 8 8"><path d="M1 1l3 3-3 3M4 1l3 3-3 3" fill="none" stroke="#fff" stroke-width="1.2"/></svg>Home</li>
        <li><svg viewBox="0 0 8 8"><path d="M1 1l3 3-3 3M4 1l3 3-3 3" fill="none" stroke="#fff" stroke-width="1.2"/></svg>About us</li>
        <li><svg viewBox="0 0 8 8"><path d="M1 1l3 3-3 3M4 1l3 3-3 3" fill="none" stroke="#fff" stroke-width="1.2"/></svg>Services</li>
        <li><svg viewBox="0 0 8 8"><path d="M1 1l3 3-3 3M4 1l3 3-3 3" fill="none" stroke="#fff" stroke-width="1.2"/></svg>Lawn care</li>
        <li><svg viewBox="0 0 8 8"><path d="M1 1l3 3-3 3M4 1l3 3-3 3" fill="none" stroke="#fff" stroke-width="1.2"/></svg>Seasonal care</li>
        <li><svg viewBox="0 0 8 8"><path d="M1 1l3 3-3 3M4 1l3 3-3 3" fill="none" stroke="#fff" stroke-width="1.2"/></svg>Hydroseeding</li>
        <li><svg viewBox="0 0 8 8"><path d="M1 1l3 3-3 3M4 1l3 3-3 3" fill="none" stroke="#fff" stroke-width="1.2"/></svg>FAQs</li>
        <li><svg viewBox="0 0 8 8"><path d="M1 1l3 3-3 3M4 1l3 3-3 3" fill="none" stroke="#fff" stroke-width="1.2"/></svg>Before &amp; After Gallery</li>
        <li><svg viewBox="0 0 8 8"><path d="M1 1l3 3-3 3M4 1l3 3-3 3" fill="none" stroke="#fff" stroke-width="1.2"/></svg>Quote / Contact</li>
      </ul>
    </div>
    <div class="badge" aria-label="Qualification badge"><div class="badge-shape"></div></div>
    <div class="contact">
      <h4>Contact Us</h4>
      <p>Get a quote for your new lawn!<br>Fill in the form or phone us on 0800 44 62 19.</p>
      <div class="form">
        <div class="field">First Name</div><div class="field">Last Name</div>
        <div class="field">Email Address</div><div class="field">Phone</div>
        <div class="field wide">Details</div>
      </div>
      <div class="btn-call">CALL ME BACK</div>
    </div>
  </div>
  <div class="grass-strip" role="img" aria-label="Strip of tall green grass blades along the page bottom"></div>
</footer>

</body>
</html>
```